Fitness competition business needs a card design

I need a professional business card design using my logo. The card will be horizontal with rounded edges.

Target Market(s)

Female fitness competitors

Industry/Entity Type

Fitness

Contact Information for Business Card

Rose-Lynn Darby
Owner
stagevarno.com
555.301.2187
info@stagevarno.com

Font styles to use
Serif

Colors

Designer to choose colors to be used in the design.

Requirements
Must have
• On the back please add the following:
• Figure
• Bikini
• Physique
• Fitness
Nice to have
• Looking for a very sleek design, contemporary and easy to read.
Should not have
• Should not be difficult to read or be too busy

```html
<!DOCTYPE html>
<html lang="en">
<head>
<meta charset="utf-8">
<title>Stage Varno – Business Cards</title>
<link rel="stylesheet" href="https://fonts.googleapis.com/css2?family=Black+Ops+One&family=Roboto:wght@400;500;700&display=swap">
<style>
  :root {
    --brand-red: #ec2027;
    --brand-grey: #58595b;
    --paper: #ffffff;
    --stage-bg: #e9e9ea;
    --ink-light: #ffffff;
  }
  * { margin: 0; padding: 0; box-sizing: border-box; }
  html, body { width: 1200px; height: 900px; overflow: hidden; }
  body {
    background: var(--stage-bg);
    font-family: "Roboto", Arial, sans-serif;
    position: relative;
  }
  .card {
    position: absolute;
    width: 620px;
    height: 354px;
    border-radius: 22px;
    overflow: hidden;
    box-shadow: 0 8px 24px rgba(0,0,0,0.18);
  }

  /* Back of card */
  .card-back {
    left: 60px;
    top: 60px;
    background: var(--brand-red);
    color: var(--ink-light);
  }
  .brand-mark {
    position: absolute;
    left: 0; right: 0;
    top: 104px;
    display: flex;
    align-items: center;
    justify-content: center;
    gap: 14px;
  }
  .brand-square {
    width: 26px; height: 26px;
    background: var(--brand-grey);
  }
  .brand-name {
    font-family: "Roboto", Arial, sans-serif;
    font-weight: 700;
    font-size: 50px;
    letter-spacing: 2px;
    text-transform: uppercase;
  }
  .card-back .brand-name { color: var(--ink-light); }
  .category-list {
    position: absolute;
    left: 40px; right: 40px;
    top: 222px;
    display: flex;
    justify-content: space-between;
    list-style: none;
    font-family: "Black Ops One", Impact, sans-serif;
    font-size: 19px;
    letter-spacing: 1px;
  }
  .back-website {
    position: absolute;
    left: 0; right: 0;
    top: 286px;
    text-align: center;
    font-size: 15px;
    letter-spacing: 0.5px;
  }

  /* Front of card */
  .card-front {
    left: 520px;
    top: 486px;
    background: var(--paper);
  }
  .front-waves {
    position: absolute;
    inset: 0;
    width: 620px;
    height: 354px;
  }
  .holder {
    position: absolute;
    left: 34px;
    top: 74px;
  }
  .holder-name {
    color: var(--brand-red);
    font-size: 24px;
    font-weight: 500;
  }
  .holder-role {
    color: var(--brand-grey);
    font-size: 11px;
    letter-spacing: 0.5px;
    margin-top: 4px;
  }
  .card-front .brand-mark {
    left: auto;
    right: 30px;
    top: 36px;
    gap: 10px;
  }
  .card-front .brand-name {
    color: var(--brand-red);
    font-size: 34px;
  }
  .card-front .brand-square { width: 18px; height: 18px; }
  .address {
    position: absolute;
    right: 30px;
    top: 186px;
    color: var(--ink-light);
    font-size: 13px;
    line-height: 1.4;
    text-align: right;
  }
  .address svg { display: block; margin: 0 0 4px auto; }
  .contact-list {
    position: absolute;
    left: 34px;
    bottom: 30px;
    list-style: none;
    color: var(--ink-light);
    font-size: 15px;
  }
  .contact-list li {
    display: flex;
    align-items: center;
    gap: 12px;
    margin-top: 7px;
  }
  .contact-icon {
    width: 22px; height: 22px;
    background: var(--paper);
    display: flex;
    align-items: center;
    justify-content: center;
  }
</style>
</head>
<body>

  <section class="card card-back" aria-label="Card back">
    <div class="brand-mark">
      <span class="brand-square"></span>
      <span class="brand-name">Stage Varno</span>
    </div>
    <ul class="category-list">
      <li>FIGURE</li>
      <li>BIKINI</li>
      <li>PHYSIQUE</li>
      <li>FITNESS</li>
    </ul>
    <p class="back-website">stagevarno.com</p>
  </section>

  <section class="card card-front" aria-label="Card front">
    <svg class="front-waves" viewBox="0 0 620 354" aria-hidden="true">
      <path d="M0 354 L0 238 C110 150 240 128 360 150 C460 168 560 150 620 70 L620 354 Z" fill="var(--brand-red)"/>
      <path d="M620 52 C580 120 500 150 360 144 C480 148 570 128 620 74 Z" fill="var(--brand-grey)"/>
      <path d="M0 238 C70 180 150 148 270 136 C160 152 80 190 0 254 Z" fill="var(--brand-grey)"/>
    </svg>

    <div class="holder">
      <p class="holder-name">Rose-Lynn Darby</p>
      <p class="holder-role">OWNER</p>
    </div>

    <div class="brand-mark">
      <span class="brand-square"></span>
      <span class="brand-name">Stage Varno</span>
    </div>

    <address class="address" style="font-style: normal;">
      <svg width="12" height="16" viewBox="0 0 12 16"><path d="M6 0a6 6 0 0 0-6 6c0 4.5 6 10 6 10s6-5.5 6-10a6 6 0 0 0-6-6zm0 8.2A2.2 2.2 0 1 1 6 3.8a2.2 2.2 0 0 1 0 4.4z" fill="var(--ink-light)"/></svg>
      1234 Your full address<br>Harlow Bay, ABC 123
    </address>

    <ul class="contact-list">
      <li>
        <span class="contact-icon"><svg width="14" height="14" viewBox="0 0 24 24"><path d="M6.6 10.8a15.1 15.1 0 0 0 6.6 6.6l2.2-2.2c.3-.3.7-.4 1-.2 1.1.4 2.3.6 3.6.6.6 0 1 .4 1 1V20c0 .6-.4 1-1 1A17 17 0 0 1 3 4c0-.6.4-1 1-1h3.5c.6 0 1 .4 1 1 0 1.3.2 2.5.6 3.6.1.3 0 .7-.2 1z" fill="var(--brand-red)"/></svg></span>
        555.301.2187
      </li>
      <li>
        <span class="contact-icon"><svg width="14" height="12" viewBox="0 0 14 12"><rect x="0.5" y="0.5" width="13" height="11" fill="none" stroke="var(--brand-red)"/><path d="M0.5 0.5 L7 6.5 L13.5 0.5" fill="none" stroke="var(--brand-red)"/></svg></span>
        info@stagevarno.com
      </li>
      <li>
        <span class="contact-icon"><svg width="14" height="14" viewBox="0 0 14 14"><circle cx="7" cy="7" r="6" fill="none" stroke="var(--brand-red)" stroke-width="1.4"/><path d="M1 7h12M7 1c-2.5 3-2.5 9 0 12M7 1c2.5 3 2.5 9 0 12" fill="none" stroke="var(--brand-red)"/></svg></span>
        stagevarno.com
      </li>
    </ul>
  </section>

</body>
</html>
```